Advertisement Sign

Hello,
We're in need of a new design for an advertisement sign. Below is our current concept, but we're looking for improvements. Specifically, we'd like to enhance the size of the 'Call for Assistance' text, possibly explore different fonts, and possibly add a background to make the design more engaging and less plain. We need something that sticks out more. Any suggestions are welcome.

Target Market(s)

Construction and Landscape Companies

```html
<!DOCTYPE html>
<html lang="en">
<head>
<meta charset="utf-8">
<title>Ridgeway Equipment Rentals – Yard Sign</title>
<link rel="stylesheet" href="https://fonts.googleapis.com/css2?family=Exo+2:wght@800&family=Michroma&family=Saira+Condensed:wght@700&display=swap">
<style>
  :root {
    --backdrop: #8f8f8f;
    --ink: #222222;
    --brand-blue: #1a78d0;
    --sky-blue: #29a8e0;
    --slate: #6a6a6a;
    --white: #ffffff;
    --silver-light: #f7f7f7;
    --silver-mid: #d9d9d9;
  }
  * { margin: 0; padding: 0; box-sizing: border-box; }
  html, body {
    width: 928px;
    height: 1200px;
    overflow: hidden;
    background: var(--backdrop);
  }
  .canvas {
    position: relative;
    width: 928px;
    height: 1200px;
  }
  .yard-sign {
    position: absolute;
    left: 34px;
    top: 380px;
    width: 860px;
    height: 439px;
    display: block;
  }
  .wordmark {
    font-family: "Exo 2", sans-serif;
    font-weight: 800;
    fill: var(--ink);
  }
  .tagline {
    font-family: "Michroma", sans-serif;
    fill: var(--slate);
  }
  .call-heading {
    font-family: "Saira Condensed", sans-serif;
    font-weight: 700;
    fill: var(--brand-blue);
  }
  .phone-number {
    font-family: "Exo 2", sans-serif;
    font-weight: 800;
    fill: var(--white);
  }
</style>
</head>
<body>
<main class="canvas">
  <svg class="yard-sign" viewBox="0 0 1410 720" xmlns="http://www.w3.org/2000/svg" aria-labelledby="sign-title">
    <title id="sign-title">Ridgeway Equipment Rentals – call for assistance 403-555-0148</title>
    <defs>
      <linearGradient id="silver" x1="0" y1="0" x2="1" y2="0">
        <stop offset="0" stop-color="var(--silver-mid)"/>
        <stop offset="0.12" stop-color="var(--silver-light)"/>
        <stop offset="0.3" stop-color="var(--silver-mid)"/>
        <stop offset="0.5" stop-color="var(--silver-light)"/>
        <stop offset="0.68" stop-color="var(--silver-mid)"/>
        <stop offset="0.85" stop-color="var(--silver-light)"/>
        <stop offset="1" stop-color="var(--silver-mid)"/>
      </linearGradient>
    </defs>

    <rect class="board" x="0" y="0" width="1410" height="720" fill="var(--white)"/>

    <rect class="top-band" x="0" y="0" width="1410" height="37" fill="var(--sky-blue)" role="img" aria-label="Blue and black hazard stripe border"/>

    <rect class="brand-panel" x="0" y="45" width="1410" height="380" fill="url(#silver)"/>
    <rect class="brand-square" x="150" y="175" width="150" height="150" fill="var(--brand-blue)"/>
    <text class="wordmark" x="380" y="250" font-size="120" textLength="890" lengthAdjust="spacingAndGlyphs">RIDGEWAY</text>
    <text class="wordmark" x="382" y="314" font-size="44" textLength="886" lengthAdjust="spacing">EQUIPMENT RENTALS</text>
    <rect class="tagline-rule" x="385" y="350" width="150" height="4" fill="var(--slate)"/>
    <text class="tagline" x="580" y="362" font-size="24" textLength="490" lengthAdjust="spacing">BUILT FOR THE JOB</text>
    <rect class="tagline-rule" x="1115" y="350" width="150" height="4" fill="var(--slate)"/>

    <rect class="call-band-sides" x="0" y="460" width="1410" height="260" fill="var(--brand-blue)"/>
    <polygon class="call-band-border" points="38,458 1392,458 1337,590 1405,720 43,720 85,590" fill="var(--white)"/>
    <rect class="call-top-band" x="90" y="438" width="1270" height="20" fill="var(--sky-blue)" role="img" aria-label="Blue and black hazard stripe border"/>
    <polygon class="call-band" points="65,458 1365,458 1310,590 1380,720 68,720 110,590" fill="var(--ink)"/>

    <polygon class="accent-rule" points="120,514 245,506 245,516" fill="var(--sky-blue)"/>
    <text class="call-heading" x="280" y="542" font-size="80" textLength="850" lengthAdjust="spacingAndGlyphs">CALL FOR ASSISTANCE</text>
    <polygon class="accent-rule" points="1165,506 1290,514 1165,516" fill="var(--sky-blue)"/>

    <text class="phone-number" x="150" y="702" font-size="190" textLength="1115" lengthAdjust="spacingAndGlyphs">403-555-0148</text>
  </svg>
</main>
</body>
</html>
```